Design für Geburtskarte A6 hoch, Klappkarte
Zielgruppe
Ich bin Fotograf und habe mich auf Schwangerschafts- und Neugeborenenfotografie spezialisiert. Meine Zielgruppe sind schwangere Frauen im letzten Drittel der Schwangerschaft und frisch gewordene Eltern.
Aufgabenstellung
- sehr schlichtes Design, in der Anlage finden Sie zwei der meist verkauften Karten damit Sie sich vom Stil eine Vorstellung machen können
- Lieferung als offene Indesign 5.5 Datei (so das die Farben, Texte, .... angepasst werden können)
- 2-3 Bilder (querformat) sollen in das Design eingearbeitet werden können
- Die Karten werden von mir nachher als fertig gedruckte Karte an meine Kunden verkauft, dies bitte ich zu berücksichtigen
- ich möchte die Karten so nutzen können das sowohl Geburtskarten für Jungs wie auch für Mädels erstellt werden können
- Format: Din A6 (geschlossen 105x148mm), Klappkarte, hoch, 3mm Beschnitt

```html
<!DOCTYPE html>
<html lang="de">
<head>
<meta charset="utf-8">
<title>Geburtskarte Danke – Klappkarte</title>
<link rel="stylesheet" href="https://fonts.googleapis.com/css2?family=Rokkitt:wght@300;400&family=Jost:wght@300&display=swap">
<style>
  :root{
    --page:#efefef;
    --teal:#6b959c;
    --mint:#a5cbc3;
    --mint-dark:#8db8af;
    --white:#ffffff;
    --photo-light:#e6e6e6;
    --photo-mid:#a9a9a9;
    --photo-dark:#4a4a4a;
  }
  *{margin:0;padding:0;box-sizing:border-box}
  html,body{width:1200px;height:829px;overflow:hidden}
  body{background:var(--page);position:relative;font-family:'Jost',sans-serif;color:var(--white)}
  .spread{position:absolute;top:215px;width:565px;height:398px;background:var(--teal);box-shadow:0 2px 10px rgba(0,0,0,.12)}
  .spread--outside{left:25px}
  .spread--inside{left:610px}
  .photo{position:absolute}
  .outside-photos{position:absolute;left:282.5px;top:0;width:282.5px;height:398px;background:var(--white)}
  .cover-photo{left:0;top:0;width:282.5px;height:242px;background:linear-gradient(150deg,var(--photo-mid),var(--photo-dark) 70%,#5e5e5e)}
  .back-photo{left:0;top:254px;width:282.5px;height:144px;background:linear-gradient(100deg,#6a6a6a,var(--photo-light) 60%,#f4f4f4)}
  .baby-name{position:absolute;right:22px;top:196px;font-family:'Rokkitt',serif;font-weight:300;font-size:34px;letter-spacing:1px}
  .inside-photo-top{left:15px;top:14px;width:252px;height:216px;background:linear-gradient(160deg,#efefef,#d4d4d4 55%,#bdbdbd)}
  .inside-photo-bottom{left:15px;top:244px;width:252px;height:141px;background:linear-gradient(110deg,#555,#c8c8c8 50%,#e8e8e8)}
  .message{position:absolute;left:310px;width:228px;top:60px;text-align:center}
  .message h1{font-family:'Rokkitt',serif;font-weight:300;font-size:36px;letter-spacing:2px;line-height:1}
  .message .thanks{margin-top:12px;font-size:11px;line-height:14px;font-weight:300}
  .message .parents{margin-top:12px;font-size:11px;font-weight:300}
  .message .heart{display:block;margin:5px auto 0}
  .facts{position:absolute;left:310px;width:232px;font-family:'Rokkitt',serif;font-weight:300;font-size:14px;letter-spacing:1px}
  .facts-row{position:absolute;left:0;width:232px;height:24px}
  .facts-row span{position:absolute;top:3px}
  .row-time{top:274px}
  .row-size{top:319px}
  .ruler{position:absolute;left:0;top:301px}
</style>
</head>
<body>
  <section class="spread spread--outside" aria-label="Außenseite">
    <div class="outside-photos">
      <div class="photo cover-photo" role="img" aria-label="Schwarzweißfoto: Neugeborenes mit Strickmütze"></div>
      <div class="baby-name">Jonas</div>
      <div class="photo back-photo" role="img" aria-label="Schwarzweißfoto: Neugeborenes schaut in die Kamera"></div>
    </div>
  </section>

  <section class="spread spread--inside" aria-label="Innenseite">
    <div class="photo inside-photo-top" role="img" aria-label="Schwarzweißfoto: schlafendes Neugeborenes auf einer Decke"></div>
    <div class="photo inside-photo-bottom" role="img" aria-label="Schwarzweißfoto: Neugeborenes schläft auf dem Bauch"></div>

    <div class="message">
      <h1>Danke</h1>
      <p class="thanks">für die Glückwünsche und Geschenke<br>zur Geburt unseres Sohnes.</p>
      <p class="parents">Mia &amp; Tom</p>
      <svg class="heart" width="14" height="14" viewBox="0 0 14 14" aria-hidden="true">
        <circle cx="7" cy="7" r="7" fill="var(--mint)"/>
        <path d="M7 11 L3.6 7.4 A2 2 0 0 1 7 4.6 A2 2 0 0 1 10.4 7.4 Z" fill="var(--white)"/>
      </svg>
    </div>

    <div class="facts">
      <div class="facts-row row-time">
        <span style="left:0">24. Juni 2016</span>
        <svg style="position:absolute;left:114px;top:0" width="22" height="22" viewBox="0 0 22 22" aria-hidden="true">
          <circle cx="11" cy="11" r="10" fill="var(--white)" stroke="#e0e0e0"/>
          <path d="M11 4.5 V11 L8 14" stroke="#333" stroke-width="1.6" fill="none" stroke-linecap="round"/>
        </svg>
        <span style="left:150px">17.03 Uhr</span>
      </div>
      <svg class="ruler" width="230" height="10" viewBox="0 0 230 10" aria-hidden="true">
        <rect x="0" y="1" width="230" height="8" fill="var(--mint)"/>
        <g stroke="var(--teal)" stroke-width="1">
          <line x1="7" y1="1" x2="7" y2="5"/><line x1="19" y1="1" x2="19" y2="4"/><line x1="31" y1="1" x2="31" y2="5"/><line x1="43" y1="1" x2="43" y2="4"/><line x1="55" y1="1" x2="55" y2="5"/><line x1="67" y1="1" x2="67" y2="4"/><line x1="79" y1="1" x2="79" y2="5"/><line x1="91" y1="1" x2="91" y2="4"/><line x1="103" y1="1" x2="103" y2="5"/><line x1="115" y1="1" x2="115" y2="4"/><line x1="127" y1="1" x2="127" y2="5"/><line x1="139" y1="1" x2="139" y2="4"/><line x1="151" y1="1" x2="151" y2="5"/><line x1="163" y1="1" x2="163" y2="4"/><line x1="175" y1="1" x2="175" y2="5"/><line x1="187" y1="1" x2="187" y2="4"/><line x1="199" y1="1" x2="199" y2="5"/><line x1="211" y1="1" x2="211" y2="4"/><line x1="223" y1="1" x2="223" y2="5"/>
        </g>
      </svg>
      <div class="facts-row row-size">
        <span style="left:0">3690 Gramm</span>
        <svg style="position:absolute;left:116px;top:-2px" width="24" height="26" viewBox="0 0 24 26" aria-hidden="true">
          <path d="M2 1 H22 L15 10 H9 Z" fill="var(--mint)"/>
          <path d="M9 12 H15 L22 25 H2 Z" fill="var(--mint)"/>
          <circle cx="12" cy="18" r="4" fill="var(--white)"/>
          <line x1="12" y1="18" x2="12" y2="15.5" stroke="#333" stroke-width="1"/>
        </svg>
        <span style="left:150px">52&nbsp;&nbsp;cm</span>
      </div>
    </div>
  </section>
</body>
</html>
```